Create a memorable Stationary for Security Software Company

TelVandrik is the worldwide leader in securing the Internet. Making Internet communications and critical data secure, reliable and available everywhere has been and continues to be our ongoing vision. We are committed to staying focused on real customer needs and to developing new and innovative security solutions that redefine the security landscape.

Industry/Entity Type

Internet

Font styles to use
Serif
Sans Serif
Script

Colors
0792cd
33a6d7
85cae6

```html
<!DOCTYPE html>
<html lang="en">
<head>
<meta charset="utf-8">
<title>TelVandrik Stationery</title>
<link href="https://fonts.googleapis.com/css2?family=Open+Sans:wght@400;600;700&display=swap" rel="stylesheet">
<style>
  :root {
    --blue-deep: #0792cd;
    --blue-mid: #33a6d7;
    --blue-light: #85cae6;
    --paper: #ffffff;
    --ink: #3a3f45;
    --ink-soft: #7a8088;
    --backdrop: #e6e8eb;
  }
  * { box-sizing: border-box; margin: 0; padding: 0; }
  html, body { width: 1200px; height: 3291px; overflow: hidden; }
  body { background: var(--backdrop); font-family: "Open Sans", Arial, sans-serif; color: var(--ink); position: relative; }

  .sheet { position: absolute; background: var(--paper); overflow: hidden; box-shadow: 0 6px 22px rgba(0,0,0,.12); }
  .sheet > svg.shapes { position: absolute; inset: 0; width: 100%; height: 100%; }

  .brand { position: absolute; display: flex; align-items: center; gap: 10px; color: var(--blue-deep); font-weight: 600; white-space: nowrap; }
  .brand-dot { border-radius: 50%; background: var(--blue-deep); flex: none; }

  .accent-bar { position: absolute; left: 0; width: 7px; background: var(--blue-deep); }

  .contacts { position: absolute; list-style: none; }
  .contacts li { display: flex; align-items: center; gap: 8px; white-space: nowrap; }
  .contacts svg { flex: none; fill: var(--blue-deep); }

  /* letterhead */
  .letterhead { left: 60px; top: 60px; width: 680px; height: 962px; }
  .letterhead .brand { left: 250px; top: 52px; font-size: 26px; }
  .letterhead .brand-dot { width: 34px; height: 34px; }
  .letter-body { position: absolute; left: 70px; top: 230px; width: 540px; font-size: 12.5px; line-height: 1.75; color: var(--ink-soft); }
  .letter-body p { margin-bottom: 14px; }
  .letterhead .accent-bar { top: 842px; height: 62px; }
  .letterhead .contacts { left: 30px; top: 842px; font-size: 11px; color: var(--ink-soft); }
  .letterhead .contacts li { height: 21px; }
  .letterhead .contacts.right { left: 250px; }

  /* business cards */
  .card-front-small { left: 800px; top: 240px; width: 340px; height: 194px; }
  .card-back-small { left: 800px; top: 520px; width: 340px; height: 194px; }
  .card-front { left: 60px; top: 1110px; width: 520px; height: 297px; }
  .card-back { left: 620px; top: 1110px; width: 520px; height: 297px; }

  .card-front .brand, .card-front-small .brand { left: 50%; top: 50%; transform: translate(-50%,-50%); }
  .card-front .brand { font-size: 30px; }
  .card-front .brand-dot { width: 38px; height: 38px; }
  .card-front-small .brand { font-size: 20px; gap: 7px; }
  .card-front-small .brand-dot { width: 24px; height: 24px; }

  .card-back .person { position: absolute; left: 34px; top: 36px; }
  .person-name { font-weight: 700; color: var(--ink); }
  .person-role { color: var(--blue-deep); }
  .card-back .person-name { font-size: 19px; }
  .card-back .person-role { font-size: 13px; }
  .card-back .brand { right: 40px; top: 40px; font-size: 18px; gap: 7px; }
  .card-back .brand-dot { width: 22px; height: 22px; }
  .card-back .accent-bar { top: 146px; height: 118px; }
  .card-back .contacts { left: 34px; top: 146px; font-size: 13px; font-weight: 600; color: var(--ink); }
  .card-back .contacts li { height: 23.6px; }

  .card-back-small .person { position: absolute; left: 22px; top: 22px; }
  .card-back-small .person-name { font-size: 13px; }
  .card-back-small .person-role { font-size: 9px; }
  .card-back-small .brand { right: 26px; top: 26px; font-size: 12px; gap: 5px; }
  .card-back-small .brand-dot { width: 14px; height: 14px; }
  .card-back-small .accent-bar { top: 96px; height: 76px; width: 5px; }
  .card-back-small .contacts { left: 22px; top: 96px; font-size: 8.5px; font-weight: 600; }
  .card-back-small .contacts li { height: 15.2px; gap: 6px; }

  /* cover sheet */
  .cover { left: 260px; top: 1500px; width: 680px; height: 962px; }
  .cover .brand { left: 50%; top: 46%; transform: translate(-50%,-50%); font-size: 42px; gap: 14px; }
  .cover .brand-dot { width: 54px; height: 54px; }

  /* envelope */
  .envelope { left: 60px; top: 2560px; width: 1080px; height: 514px; }
  .envelope .brand { left: 220px; top: 60px; font-size: 32px; }
  .envelope .brand-dot { width: 40px; height: 40px; }
  .envelope .accent-bar { top: 214px; height: 46px; width: 10px; }
  .return-line { position: absolute; left: 40px; top: 226px; font-size: 15px; color: var(--ink-soft); }
  .return-line .return-address { color: var(--blue-deep); }
</style>
</head>
<body>

<svg width="0" height="0" style="position:absolute">
  <defs>
    <symbol id="icon-pin" viewBox="0 0 12 12"><path d="M6 0.5a4 4 0 0 0-4 4c0 3 4 7 4 7s4-4 4-7a4 4 0 0 0-4-4zm0 5.5a1.5 1.5 0 1 1 0-3 1.5 1.5 0 0 1 0 3z"/></symbol>
    <symbol id="icon-mail" viewBox="0 0 12 12"><path d="M1 2.5h10v7H1z M1.6 3l4.4 3.4L10.4 3" stroke="#fff" stroke-width="0.9"/></symbol>
    <symbol id="icon-phone" viewBox="0 0 12 12"><path d="M3 1l2 2.4-1.2 1.2a6 6 0 0 0 3.6 3.6L8.6 7 11 9l-1.4 1.8C5.4 10.6 1.4 6.6 1.2 2.4z"/></symbol>
    <symbol id="icon-web" viewBox="0 0 12 12"><circle cx="6" cy="6" r="5"/><path d="M1 6h10M6 1c2 2.5 2 7.5 0 10M6 1c-2 2.5-2 7.5 0 10" stroke="#fff" stroke-width="0.8" fill="none"/></symbol>
  </defs>
</svg>

<!-- Letterhead -->
<section class="sheet letterhead">
  <svg class="shapes" viewBox="0 0 680 962" preserveAspectRatio="none" aria-hidden="true">
    <path d="M0 0H680V176C560 126 430 160 310 116C210 80 100 62 0 96Z" fill="var(--blue-light)"/>
    <path d="M0 112C110 82 210 98 320 134C440 174 560 146 680 196" fill="none" stroke="var(--blue-deep)" stroke-width="6"/>
    <path d="M680 962H360C470 940 570 890 680 790Z" fill="var(--blue-light)"/>
    <path d="M340 946C460 920 570 870 680 772" fill="none" stroke="var(--blue-mid)" stroke-width="5"/>
  </svg>
  <div class="brand"><span class="brand-dot"></span>TelVandrik</div>
  <div class="letter-body">
    <p>Dear Client,</p>
    <p>Thank you for choosing our team to protect your network and data. This letter confirms the start of your new security plan and outlines the steps we will take together over the coming weeks.</p>
    <p>Our engineers will review your current systems, close open gaps and set up continuous monitoring. You will receive a short report each month with clear findings and simple advice for your staff.</p>
    <p>Our service covers firewalls, encrypted mail, secure remote access and regular backup checks for every office location you operate.</p>
    <p>If you have any questions, our support desk is open day and night. We look forward to keeping your communications secure, reliable and available everywhere.</p>
    <p>Kind regards,</p>
  </div>
  <span class="accent-bar"></span>
  <ul class="contacts">
    <li><svg width="10" height="10"><use href="#icon-pin"/></svg>14 PO BOX 7310, Lindenford 5021</li>
    <li><svg width="10" height="10"><use href="#icon-mail"/></svg>info@telvandrik.com</li>
  </ul>
  <ul class="contacts right">
    <li><svg width="10" height="10"><use href="#icon-phone"/></svg>1300 562 804 / (07) 4821 3095</li>
    <li><svg width="10" height="10"><use href="#icon-web"/></svg>www.telvandrik.com</li>
  </ul>
</section>

<!-- Small business card, front -->
<section class="sheet card-front-small">
  <svg class="shapes" viewBox="0 0 520 297" preserveAspectRatio="none" aria-hidden="true">
    <path d="M0 0H520V40C380 60 250 50 120 80C70 92 30 104 0 112Z" fill="var(--blue-light)"/>
    <path d="M0 124C110 92 230 78 360 66C430 60 480 54 520 48" fill="none" stroke="var(--blue-deep)" stroke-width="5"/>
    <path d="M0 297V250C140 210 320 226 520 180V297Z" fill="var(--blue-light)"/>
    <path d="M0 238C160 196 330 214 520 168" fill="none" stroke="var(--blue-mid)" stroke-width="4"/>
  </svg>
  <div class="brand"><span class="brand-dot"></span>TelVandrik</div>
</section>

<!-- Small business card, back -->
<section class="sheet card-back-small">
  <svg class="shapes" viewBox="0 0 520 297" preserveAspectRatio="none" aria-hidden="true">
    <path d="M520 297H300C400 270 470 200 520 110Z" fill="var(--blue-light)"/>
    <path d="M280 292C390 264 462 196 520 96" fill="none" stroke="var(--blue-deep)" stroke-width="5"/>
  </svg>
  <div class="person"><div class="person-name">Marek Holloway</div><div class="person-role">Manager</div></div>
  <div class="brand"><span class="brand-dot"></span>TelVandrik</div>
  <span class="accent-bar"></span>
  <ul class="contacts">
    <li><svg width="8" height="8"><use href="#icon-pin"/></svg>14 PO BOX 7310, Lindenford 5021</li>
    <li><svg width="8" height="8"><use href="#icon-mail"/></svg>info@telvandrik.com</li>
    <li><svg width="8" height="8"><use href="#icon-phone"/></svg>1300 562 804 / (07) 4821 3095</li>
    <li><svg width="8" height="8"><use href="#icon-web"/></svg>www.telvandrik.com</li>
  </ul>
</section>

<!-- Business card, front -->
<section class="sheet card-front">
  <svg class="shapes" viewBox="0 0 520 297" preserveAspectRatio="none" aria-hidden="true">
    <path d="M0 0H520V40C380 60 250 50 120 80C70 92 30 104 0 112Z" fill="var(--blue-light)"/>
    <path d="M0 124C110 92 230 78 360 66C430 60 480 54 520 48" fill="none" stroke="var(--blue-deep)" stroke-width="5"/>
    <path d="M0 297V250C140 210 320 226 520 180V297Z" fill="var(--blue-light)"/>
    <path d="M0 238C160 196 330 214 520 168" fill="none" stroke="var(--blue-mid)" stroke-width="4"/>
  </svg>
  <div class="brand"><span class="brand-dot"></span>TelVandrik</div>
</section>

<!-- Business card, back -->
<section class="sheet card-back">
  <svg class="shapes" viewBox="0 0 520 297" preserveAspectRatio="none" aria-hidden="true">
    <path d="M520 297H300C400 270 470 200 520 110Z" fill="var(--blue-light)"/>
    <path d="M280 292C390 264 462 196 520 96" fill="none" stroke="var(--blue-deep)" stroke-width="5"/>
  </svg>
  <div class="person"><div class="person-name">Marek Holloway</div><div class="person-role">Manager</div></div>
  <div class="brand"><span class="brand-dot"></span>TelVandrik</div>
  <span class="accent-bar"></span>
  <ul class="contacts">
    <li><svg width="12" height="12"><use href="#icon-pin"/></svg>14 PO BOX 7310, Lindenford 5021</li>
    <li><svg width="12" height="12"><use href="#icon-mail"/></svg>info@telvandrik.com</li>
    <li><svg width="12" height="12"><use href="#icon-phone"/></svg>1300 562 804 / (07) 4821 3095</li>
    <li><svg width="12" height="12"><use href="#icon-web"/></svg>www.telvandrik.com</li>
  </ul>
</section>

<!-- Cover sheet -->
<section class="sheet cover">
  <svg class="shapes" viewBox="0 0 680 962" preserveAspectRatio="none" aria-hidden="true">
    <path d="M0 0H680V60C560 110 420 150 280 130C170 114 80 120 0 150Z" fill="var(--blue-light)"/>
    <path d="M0 166C90 134 180 130 290 146C430 166 560 128 680 76" fill="none" stroke="var(--blue-deep)" stroke-width="6"/>
    <path d="M0 962V800C120 760 250 800 380 830C500 858 600 840 680 810V962Z" fill="var(--blue-light)"/>
    <path d="M0 784C120 744 250 786 380 814C500 842 600 824 680 794" fill="none" stroke="var(--blue-mid)" stroke-width="5"/>
  </svg>
  <div class="brand"><span class="brand-dot"></span>TelVandrik</div>
</section>

<!-- Envelope -->
<section class="sheet envelope">
  <svg class="shapes" viewBox="0 0 1080 514" preserveAspectRatio="none" aria-hidden="true">
    <path d="M1080 514H560C760 480 930 400 1080 260Z" fill="var(--blue-light)"/>
    <path d="M520 506C730 470 910 386 1080 236" fill="none" stroke="var(--blue-deep)" stroke-width="7"/>
  </svg>
  <div class="brand"><span class="brand-dot"></span>TelVandrik</div>
  <span class="accent-bar"></span>
  <p class="return-line">If undelivered, please return to: <span class="return-address">14 PO BOX 7310, Lindenford 5021</span></p>
</section>

</body>
</html>
```